Business card and Stationery for data intelligence company

We need a new design for our business cards and stationery (Business Letter templates and a Quote example on Word, but it MUST work on Google Doc as well).

We are a software company based in Ireland and UK. Our product is "Kovar", data intelligence platform with beautiful visualizations, graph capabilities (things are interconnected), powerful, flexible, it can manage Big Data and Streaming information. It's modern and relatively open source.
Our company will provide data intelligence for law enforcements, pharmaceuticals, and similar high end customers.

We'll launch a new website soon. At the moment it's http://www.kovar-analytics.example if you want to take a look. This is our youtube channel in case you need it to understand what Kovar is: https://www.youtube.com/c/kovaranalyticschannel

We changed the logo so please use the logo I attach here.

We'd like the output to be cool and modern but elegant and "business" at the same time. It should inspire simple sophistication, "unity" "intent" "purpose" yet subtly very advanced and innovative.

The name "Kovar" does NOT refer to sirens (mithological creatures) as well as the warning devices. It means Kinetic Object Vector Analysis Reactor. Please use our logo's colors and if you want to something like the "graph" image.

```html
<!DOCTYPE html>
<html lang="en">
<head>
<meta charset="utf-8">
<title>Kovar — Stationery Set</title>
<link href="https://fonts.googleapis.com/css2?family=Open+Sans:wght@400;600;700&display=swap" rel="stylesheet">
<style>
:root{
  --bg:#e8e8e8;
  --paper:#f3f3f2;
  --orange:#f5a623;
  --accent:#d9441c;
  --navy:#173a5e;
  --navy-deep:#112c49;
  --ink:#4a4a4a;
  --ink-soft:#6d6d6d;
  --rule:#b9b9b9;
}
*{margin:0;padding:0;box-sizing:border-box}
html,body{width:1200px;height:912px;overflow:hidden}
body{background:var(--bg);font-family:"Open Sans",Arial,sans-serif;color:var(--ink);position:relative}
.sheet{position:absolute;background:var(--paper);box-shadow:0 2px 8px rgba(0,0,0,.18)}
.brand{position:absolute;display:flex;align-items:center;gap:6px;font-family:"Open Sans",Arial,sans-serif;font-weight:600;color:var(--orange);letter-spacing:.12em;line-height:1}
.brand .dot{border-radius:50%;background:var(--orange);flex:none}

/* Letterhead */
.letterhead{left:146px;top:168px;width:429px;height:550px}
.letterhead .brand{left:24px;top:24px;font-size:27px}
.letterhead .brand .dot{width:22px;height:22px}
.contact-block{position:absolute;left:311px;top:30px;border-left:1px solid var(--rule);padding-left:14px;height:37px}
.contact-line{display:flex;align-items:center;gap:5px;font-size:7px;font-weight:600;color:var(--ink);height:12.5px}
.contact-line svg{width:7px;height:7px;flex:none}
.letter{position:absolute;left:31px;top:193px;width:370px;font-size:6.6px;line-height:7.6px;color:var(--ink)}
.letter .to{margin-bottom:9px}
.letter .recipient{font-size:9px;font-weight:600;color:var(--accent);line-height:10px}
.letter .role{font-weight:600;margin-bottom:17px}
.letter .salutation{margin-bottom:6px}
.letter p{text-align:justify;margin-bottom:8px}
.signature{position:absolute;left:31px;top:404px;width:110px;height:20px;background:linear-gradient(90deg,rgba(217,68,28,.35),rgba(217,68,28,.12));border-radius:3px}

/* Envelope front */
.envelope-front{left:659px;top:166px;width:402px;height:181px}
.envelope-front .brand{left:14px;top:23px;font-size:24px}
.envelope-front .brand .dot{width:18px;height:18px}
.return-address{position:absolute;left:17px;top:73px;font-size:5.6px;line-height:7px;color:var(--ink)}
.return-web{position:absolute;left:17px;top:92px;display:flex;align-items:center;gap:5px;font-size:6px;font-weight:600}

/* Envelope back */
.envelope-back{left:662px;top:378px;width:402px;height:180px;overflow:hidden}
.envelope-back svg.flap{position:absolute;left:0;top:0}
.flap-seal{position:absolute;left:191px;top:24px;width:20px;height:20px;border-radius:50%;border:3px solid var(--orange)}

/* Business cards */
.card-front{left:658px;top:615px;width:190px;height:109px}
.card-front .brand{left:12px;top:9px;font-size:18px}
.card-front .brand .dot{width:14px;height:14px}
.card-tab{position:absolute;left:0;top:39px;width:3px;height:13px;background:var(--orange)}
.card-name{position:absolute;left:13px;top:40px;font-size:7.5px;font-weight:700;color:#222;line-height:9px}
.card-name small{font-size:4.5px;font-weight:600}
.card-title{position:absolute;left:13px;top:49px;font-size:4.6px;color:var(--accent);font-weight:600}
.card-contacts{position:absolute;left:13px;top:62px}
.card-contacts .contact-line{font-size:4.6px;height:7.8px;gap:4px}
.card-contacts .contact-line svg{width:5px;height:5px}
.card-address{position:absolute;right:12px;top:88px;font-size:4.5px;line-height:5.6px;text-align:right;font-weight:600}
.card-back{left:902px;top:617px;width:191px;height:107px;background:var(--navy-deep);border-radius:3px}
.card-back .brand{left:40px;top:40px;font-size:24px}
.card-back .brand .dot{width:20px;height:20px}
</style>
</head>
<body>

<section class="sheet letterhead" aria-label="Letterhead">
  <div class="brand"><span class="dot"></span>KOVAR</div>
  <div class="contact-block">
    <div class="contact-line"><svg viewBox="0 0 10 10"><path d="M2 1l2 2-1 1.5c.7 1.3 1.3 1.9 2.5 2.5L7 6l2 2-1.3 1.5C4.5 9 1 5.5.5 2.3z" fill="var(--accent)"/></svg>020.714.3301</div>
    <div class="contact-line"><svg viewBox="0 0 10 10"><rect x="2.5" y="1" width="5" height="3" fill="var(--accent)"/><rect x="1" y="4" width="8" height="4" rx="1" fill="var(--accent)"/></svg>020.714.3308</div>
    <div class="contact-line"><svg viewBox="0 0 10 10"><circle cx="5" cy="5" r="4.5" fill="var(--accent)" opacity=".8"/></svg>kovar-analytics.example</div>
  </div>
  <div class="letter">
    <div class="to">To</div>
    <div class="recipient">Declan Morrow</div>
    <div class="role">Director</div>
    <div class="salutation">Dear sir</div>
    <p>Lorem ipsum dolor sit amet, consectetur adipisicing elit, sed do eiusmod tempor incididunt ut labore et dolore magna aliqua. Ut enim ad minim veniam, quis nostrud exercitation ullamco laboris nisi ut aliquip ex ea commodo consequat. Duis aute irure dolor in reprehenderit in voluptate velit esse cillum dolore eu fugiat nulla pariatur. Excep eur sint occaecat cupidatat non proident, sunt in culpa qui officia deserunt mollit anim id est laborum. Sed ut perspiciatis unde omnis iste natus error sit voluptatem.</p>
    <p>Duis aute irure dolor in reprehenderit in voluptate velit esse cillum dolore eu fugiat nulla pariatur. Excep eur sint occaecat cupidatat non proident, sunt in culpa qui officia deserunt mollit anim id est laborum. Sed ut perspiciatis unde omnis iste natus error sit voluptatem. Duis aute irure dolor in reprehenderit in voluptate velit esse cillum dolore eu fugiat nulla pariatur. Excep eur sint occaecat cupidatat non proident, sunt in culpa qui officia deserunt mollit anim id est laborum. Sed ut perspiciatis unde omnis iste natus error sit voluptatem.</p>
    <p style="margin-top:12px">Dolorem ipsum quia dolor sit amet, consectetur, adipisci velit, sed quia non numquam eius modi tempora incidunt ut labore et dolore magnam aliquam quaerat voluptatem.</p>
  </div>
  <div class="signature" role="img" aria-label="Handwritten signature of Declan Morrow"></div>
</section>

<section class="sheet envelope-front" aria-label="Envelope front">
  <div class="brand"><span class="dot"></span>KOVAR</div>
  <div class="return-address">14 Harcourt Lane, Suite 3<br>Dublin D02 X7K1</div>
  <div class="return-web"><svg viewBox="0 0 10 10" width="6" height="6"><circle cx="5" cy="5" r="4.5" fill="var(--accent)" opacity=".8"/></svg>kovar-analytics.example</div>
</section>

<section class="sheet envelope-back" aria-label="Envelope back">
  <svg class="flap" width="402" height="80" viewBox="0 0 402 80">
    <defs><linearGradient id="flapShade" x1="0" y1="0" x2="0" y2="1"><stop offset="0" stop-color="#1d4570"/><stop offset="1" stop-color="var(--navy)"/></linearGradient></defs>
    <path d="M0 0H402L394 62Q392 64 388 64H14Q10 64 8 62Z" fill="url(#flapShade)"/>
  </svg>
  <div class="flap-seal"></div>
</section>

<section class="sheet card-front" aria-label="Business card front">
  <div class="brand"><span class="dot"></span>KOVAR</div>
  <div class="card-tab"></div>
  <div class="card-name">Ines Halloran <small>(MSc, CIPP)</small></div>
  <div class="card-title">Vice President of Client Services</div>
  <div class="card-contacts">
    <div class="contact-line"><svg viewBox="0 0 10 10"><path d="M2 1l2 2-1 1.5c.7 1.3 1.3 1.9 2.5 2.5L7 6l2 2-1.3 1.5C4.5 9 1 5.5.5 2.3z" fill="var(--accent)"/></svg>020.714.3301</div>
    <div class="contact-line"><svg viewBox="0 0 10 10"><rect x="3" y="0.5" width="4" height="9" rx="1" fill="var(--accent)"/></svg>020.714.5590</div>
    <div class="contact-line"><svg viewBox="0 0 10 10"><rect x="2.5" y="1" width="5" height="3" fill="var(--accent)"/><rect x="1" y="4" width="8" height="4" rx="1" fill="var(--accent)"/></svg>020.714.3308</div>
    <div class="contact-line"><svg viewBox="0 0 10 10"><rect x="1" y="2" width="8" height="6" fill="var(--accent)"/></svg>ihalloran@kovar-analytics.example</div>
    <div class="contact-line"><svg viewBox="0 0 10 10"><circle cx="5" cy="5" r="4.5" fill="var(--accent)" opacity=".8"/></svg>kovar-analytics.example</div>
  </div>
  <div class="card-address">14 Harcourt Lane, Suite 3<br>Dublin D02 X7K1</div>
</section>

<section class="sheet card-back" aria-label="Business card back">
  <div class="brand"><span class="dot"></span>KOVAR</div>
</section>

</body>
</html>
```